IT Company Business Card Rebranding

We want to modernize our business cards massively. We want to incorporate aspects of our old business card such as the white and geometric design with the blues of another icon. Existing Logo, old business card and icon are all attached.

We are a modern IT company that provides support for new and growing technologies and want our business cards to be modern yet professional.
Updates

Note: Do not use file ICON.png in design. This is just a design we like Added Wednesday, March 9, 2016

Industry/Entity Type

Information Technology

Contact Information for Business Card

Roughly 43 : 26 or 1075 x 650 px

Font styles to use
Serif

Colors
0492cd
3276b5
33a6d7
86cfc6
cfeae6
cee9f5
ffffff

Requirements
Must have
• Modern yet professional
Nice to have
• We would like to incorporate the blues of our existing logo and of the icon provided. Really like the design of the icon.
Should not have
• Too Decorative. Just simple and professional.
• Not have the circle icon, as it is a copyrighted icon, I just like the colors and the geometric design

```html
<!DOCTYPE html>
<html lang="en">
<head>
<meta charset="utf-8">
<title>Nexa Systems Business Card</title>
<link href="https://fonts.googleapis.com/css2?family=Questrial&display=swap" rel="stylesheet">
<style>
  :root {
    --page-bg: #eceae8;
    --white: #ffffff;
    --ink: #4a4d52;
    --ink-soft: #9a9ea4;
    --blue-deep: #1f3f8f;
    --blue-mid: #3276b5;
    --blue-bright: #0492cd;
    --blue-sky: #33a6d7;
    --teal: #2bb0b8;
    --mint: #86cfc6;
  }
  * { margin: 0; padding: 0; box-sizing: border-box; }
  html, body {
    width: 1200px; height: 800px; overflow: hidden;
    background: var(--page-bg);
    font-family: "Questrial", sans-serif;
  }
  .canvas {
    width: 1200px; height: 800px;
    display: flex; align-items: center; justify-content: center; gap: 40px;
  }
  .card {
    position: relative;
    width: 540px; height: 326px;
    border-radius: 4px;
    overflow: hidden;
    box-shadow: 0 10px 28px rgba(0,0,0,0.18);
  }

  /* Back side */
  .card-back .pattern {
    position: absolute; inset: 0;
    background:
      linear-gradient(135deg, rgba(134,207,198,0.35) 0%, transparent 40%),
      linear-gradient(200deg, var(--blue-sky) 0%, var(--teal) 35%, var(--blue-mid) 70%, var(--blue-deep) 100%);
  }
  .card-back .brand {
    position: absolute; left: 0; right: 0; top: 118px;
    display: flex; align-items: center; justify-content: center; gap: 16px;
    color: var(--white);
  }
  .brand-dot {
    width: 34px; height: 34px; border-radius: 50%;
    background: var(--white);
  }
  .brand-name {
    font-size: 30px; letter-spacing: 9px; color: var(--white);
  }
  .card-back .web {
    position: absolute; left: 0; right: 0; top: 196px;
    text-align: center; color: var(--white);
    font-size: 14px; letter-spacing: 4px;
  }

  /* Front side */
  .card-front { background: var(--white); }
  .card-front svg.waves { position: absolute; inset: 0; }
  .front-brand {
    position: absolute; left: 30px; top: 30px;
    display: flex; align-items: center; gap: 14px;
  }
  .front-brand .brand-dot {
    width: 44px; height: 44px;
    background: linear-gradient(135deg, var(--blue-sky), var(--blue-deep));
  }
  .front-brand .brand-name {
    font-size: 24px; letter-spacing: 7px; color: var(--ink);
  }
  .contact {
    position: absolute; left: 30px; top: 92px;
    color: var(--ink-soft);
  }
  .contact .person {
    font-size: 17px; letter-spacing: 1.5px; text-transform: uppercase;
  }
  .contact .role { font-size: 11px; margin-top: 2px; margin-bottom: 8px; }
  .contact .line {
    display: flex; align-items: center; gap: 8px;
    font-size: 11.5px; margin-top: 4px;
  }
  .contact .icon {
    width: 13px; height: 13px; border-radius: 50%;
    background: var(--blue-sky);
    display: flex; align-items: center; justify-content: center;
  }
</style>
</head>
<body>
<main class="canvas">

  <section class="card card-back" aria-label="Card back">
    <div class="pattern" role="img" aria-label="Geometric low-poly pattern in teal and blue tones"></div>
    <div class="brand">
      <span class="brand-dot"></span>
      <span class="brand-name">NEXA SYSTEMS</span>
    </div>
    <p class="web">www.nexasystems.com</p>
  </section>

  <section class="card card-front" aria-label="Card front">
    <svg class="waves" width="540" height="326" viewBox="0 0 540 326" xmlns="http://www.w3.org/2000/svg">
      <defs>
        <linearGradient id="polyFill" x1="0" y1="0" x2="1" y2="1">
          <stop offset="0" stop-color="#33a6d7"/>
          <stop offset="0.45" stop-color="#2bb0b8"/>
          <stop offset="0.8" stop-color="#3276b5"/>
          <stop offset="1" stop-color="#1f3f8f"/>
        </linearGradient>
        <linearGradient id="bandFill" x1="0" y1="0" x2="1" y2="0">
          <stop offset="0" stop-color="#0492cd"/>
          <stop offset="1" stop-color="#1f3f8f"/>
        </linearGradient>
      </defs>
      <path role="img" aria-label="Geometric low-poly pattern in teal and blue tones"
            d="M0 224 C110 296 300 274 540 280 L540 326 L0 326 Z" fill="url(#polyFill)"/>
      <path d="M0 202 C120 274 300 252 540 258 L540 271 C300 266 115 288 0 215 Z" fill="url(#bandFill)"/>
      <path d="M0 189 C125 262 300 242 540 249 L540 252 C300 246 122 266 0 193 Z" fill="#33a6d7"/>
    </svg>

    <div class="front-brand">
      <span class="brand-dot"></span>
      <span class="brand-name">NEXA SYSTEMS</span>
    </div>

    <div class="contact">
      <p class="person">Daniel Reyes</p>
      <p class="role">Technical Services</p>
      <p class="line">
        <span class="icon">
          <svg width="8" height="8" viewBox="0 0 24 24"><path fill="#fff" d="M6.6 10.8a15 15 0 0 0 6.6 6.6l2.2-2.2a1 1 0 0 1 1-.25 11.4 11.4 0 0 0 3.6.57 1 1 0 0 1 1 1V20a1 1 0 0 1-1 1A17 17 0 0 1 3 4a1 1 0 0 1 1-1h3.5a1 1 0 0 1 1 1c0 1.25.2 2.45.57 3.57a1 1 0 0 1-.25 1z"/></svg>
        </span>
        0955 210 470
      </p>
      <p class="line">
        <span class="icon">
          <svg width="8" height="8" viewBox="0 0 24 24"><path fill="#fff" d="M2 5h20v14H2z M2 5l10 8 10-8" stroke="#33a6d7" stroke-width="2"/></svg>
        </span>
        daniel@nexasystems.com
      </p>
    </div>
  </section>

</main>
</body>
</html>
```